Website Design

Hi I would like to invite designers to re design my website .

I would like the below in brief.

On the Welcome Page.

A nice looking technical page distributed into two

SALES on one side and TECHNOLOGY on the other . once the person clicks on either of them they can explore the pages in detail.

I am keen and almost ready with information for the Technology page and would like this to begin kicking ASAP .

my current website is www.brimvoltek.net

Looking forward to seeing your feedback!

Tobiah
Updates

Hi,

 
A little more elaboration on the web front page . I need it to be more techy .

I was looking at a wheel on the Technical side or a spanner and screew driver done on flash .

Just to give you a better idea on what seperated Sales from Technology. 

Computing, Storage , Components , Peripherals , Software , TV & Gaming / Entertainment , Home & Leisure , Software , Gift Vouchers , Phones etc.

Technology .

Solar Power Solutions , Security Systems , Access Control , Automatic Gates & Turnstiles , Home/Office/Hotel Automation, Indoor and Outdoor PABX Telephony, Networking , Electricity Power Meters , IP Based Technology and ETC. 

See attached on the project updates my business card design if it can give you an idea ,also see revised Logo

```html
<!DOCTYPE html>
<html lang="en">
<head>
<meta charset="utf-8">
<title>Corvantix – Technology</title>
<link href="https://fonts.googleapis.com/css2?family=Cabin:wght@400;500;700&family=Montserrat:wght@700&display=swap" rel="stylesheet">
<style>
  :root {
    --header-bg: #f0f0f0;
    --tech-bg: #e2e2e2;
    --footer-bg: #c9c9c9;
    --brand-red: #e8161b;
    --label-red: #8e1c1c;
    --ink: #111111;
    --nav-ink: #222222;
    --muted: #555555;
  }
  * { margin: 0; padding: 0; box-sizing: border-box; }
  html, body { width: 950px; height: 1200px; overflow: hidden; }
  body { position: relative; font-family: "Cabin", sans-serif; background: #ffffff; }

  .site-header { position: absolute; left: 0; top: 0; width: 950px; height: 112px; background: var(--header-bg); }
  .brand { position: absolute; left: 78px; top: 32px; display: flex; align-items: center; gap: 10px;
    font-family: "Cabin", sans-serif; font-weight: 700; font-size: 40px; color: var(--brand-red); line-height: 1; }
  .brand-mark { width: 14px; height: 14px; border-radius: 50%; background: var(--brand-red); }
  .main-nav { position: absolute; left: 520px; top: 40px; display: flex; align-items: center; font-size: 11px; color: var(--nav-ink); }
  .main-nav a { color: inherit; text-decoration: none; margin-right: 10px; }
  .main-nav a.is-active { display: inline-block; width: 60px; height: 26px; line-height: 26px; text-align: center; color: #fff; background: linear-gradient(#4a4a4a, #050505); border-radius: 2px; margin-right: 5px; }
  .main-nav a.contact { margin-left: 7px; }

  .technology { position: absolute; left: 0; top: 112px; width: 950px; height: 489px; background-color: var(--tech-bg);
    background-image: radial-gradient(rgba(0,0,0,.05) 1px, transparent 1px); background-size: 3px 3px; }
  .tech-title { position: absolute; left: 0; width: 928px; top: 241px; text-align: center; font-family: "Montserrat", sans-serif; font-weight: 700; font-size: 26px; color: var(--brand-red); word-spacing: 10px; }
  .tech-item { position: absolute; width: 220px; margin-left: -110px; text-align: center; }
  .tech-item svg { display: block; margin: 0 auto; }
  .tech-label { position: absolute; width: 240px; margin-left: -120px; text-align: center; font-size: 13.5px; color: var(--label-red); white-space: nowrap; }

  .sales { position: absolute; left: 0; top: 601px; width: 950px; height: 527px;
    background:
      radial-gradient(ellipse 260px 320px at 420px 360px, rgba(40,40,44,.85), rgba(40,40,44,0) 70%),
      radial-gradient(ellipse 200px 160px at 470px 140px, rgba(226,196,150,.7), rgba(226,196,150,0) 75%),
      radial-gradient(ellipse 220px 200px at 640px 300px, rgba(235,238,246,.9), rgba(235,238,246,0) 75%),
      linear-gradient(100deg, #f5f6f7 0%, #e9ecee 35%, #efece8 70%, #f6f3ef 100%); }
  .sales-title { position: absolute; left: 104px; top: 82px; font-family: "Montserrat", sans-serif; font-weight: 700; font-size: 40px; color: var(--brand-red); letter-spacing: 1px; }

  .site-footer { position: absolute; left: 0; top: 1128px; width: 950px; height: 72px; background: var(--footer-bg); }
  .footer-nav { position: absolute; left: 75px; top: 12px; font-size: 11px; color: var(--nav-ink); }
  .footer-nav a { color: inherit; text-decoration: none; margin-right: 9px; }
  .footer-nav a.contact { margin-left: 8px; }
  .copyright { position: absolute; left: 75px; top: 41px; font-size: 9px; color: var(--muted); }
  .social { position: absolute; left: 748px; top: 13px; display: flex; gap: 1px; }
  .social span { width: 30px; height: 30px; border-radius: 50%; background: var(--ink); display: block; }
</style>
</head>
<body>
  <header class="site-header">
    <div class="brand"><span>Corvantix</span><span class="brand-mark"></span></div>
    <nav class="main-nav">
      <a class="is-active" href="#">Home</a>
      <a href="#">About us</a>
      <a href="#">Technology</a>
      <a href="#">Services</a>
      <a href="#">Products</a>
      <a class="contact" href="#">Contact us</a>
    </nav>
  </header>

  <section class="technology">
    <div class="tech-item" style="left:230px;top:52px">
      <svg width="68" height="64" viewBox="0 0 68 64" fill="none" stroke="#111" stroke-width="2.5">
        <path d="M8 12h44l6 28H2z"/><path d="M5 26h50M16 12l-3 28M28 12v28M40 12l3 28"/>
        <path d="M30 40v18M20 60h20" stroke-width="4"/>
        <circle cx="58" cy="12" r="4"/><path d="M58 2v3M66 12h-3M64 5l-2 2"/>
      </svg>
    </div>
    <div class="tech-label" style="left:232px;top:133px">Solar Power Solutions</div>

    <div class="tech-item" style="left:427px;top:36px">
      <svg width="72" height="72" viewBox="0 0 72 72" fill="#111">
        <circle cx="12" cy="10" r="7"/><circle cx="33" cy="10" r="7"/><circle cx="54" cy="10" r="7"/>
        <rect x="2" y="20" width="62" height="46" rx="5"/>
        <circle cx="52" cy="54" r="17" stroke="#e2e2e2" stroke-width="3"/>
        <rect x="45" y="51" width="14" height="11" fill="#e2e2e2"/>
        <path d="M48 51v-4a4 4 0 0 1 8 0v4" fill="none" stroke="#e2e2e2" stroke-width="2.5"/>
      </svg>
    </div>
    <div class="tech-label" style="left:428px;top:120px">Security Systems</div>

    <div class="tech-item" style="left:596px;top:32px">
      <svg width="72" height="70" viewBox="0 0 72 70" fill="#111">
        <rect x="31" y="0" width="6" height="20"/><path d="M24 18h20L34 30z"/>
        <path d="M2 38h22v12H2z"/><circle cx="52" cy="52" r="17"/>
        <rect x="45" y="51" width="14" height="11" fill="#e2e2e2"/>
        <path d="M48 51v-4a4 4 0 0 1 8 0v4" fill="none" stroke="#e2e2e2" stroke-width="2.5"/>
      </svg>
    </div>
    <div class="tech-label" style="left:597px;top:114px">Access Control</div>

    <div class="tech-item" style="left:735px;top:89px">
      <svg width="76" height="76" viewBox="0 0 76 76" fill="none" stroke="#111" stroke-width="6">
        <rect x="3" y="3" width="18" height="18" rx="5"/><rect x="55" y="3" width="18" height="18" rx="5"/>
        <rect x="3" y="55" width="18" height="18" rx="5"/><rect x="55" y="55" width="18" height="18" rx="5"/>
        <path d="M12 21v34M64 21v34M18 18l40 40"/>
      </svg>
    </div>
    <div class="tech-label" style="left:749px;top:185px">Automatic Gates &amp; Turnstiles</div>

    <div class="tech-item" style="left:182px;top:196px">
      <svg width="68" height="72" viewBox="0 0 68 72" fill="#111">
        <path d="M2 2h30v6H9v50l-7 4z"/><path d="M2 2l26 10v58L2 62z"/>
        <path d="M36 34h18v-8l12 12-12 12v-8H36z"/>
      </svg>
    </div>
    <div class="tech-label" style="left:179px;top:285px">Automatic Gates &amp; Turnstiles</div>

    <div class="tech-title">OUR TECHNOLOGY</div>

    <div class="tech-item" style="left:724px;top:224px">
      <svg width="34" height="72" viewBox="0 0 34 72" fill="none" stroke="#111" stroke-width="3.5">
        <path d="M10 46V8a7 7 0 0 1 14 0v38a13 13 0 1 1-14 0z"/>
        <circle cx="17" cy="56" r="5" fill="#111"/><path d="M17 52V16M24 14h-5M24 22h-5M24 30h-5"/>
      </svg>
    </div>
    <div class="tech-label" style="left:728px;top:314px">Home/Office/Hotel Automation</div>

    <div class="tech-item" style="left:226px;top:331px">
      <svg width="88" height="70" viewBox="0 0 88 70" fill="none" stroke="#111" stroke-width="2.5">
        <rect x="2" y="16" width="58" height="38"/><path d="M2 46h58M28 54v8M20 66h22" stroke-width="4"/>
        <rect x="60" y="2" width="26" height="66"/><path d="M66 10h14M66 16h14M66 22h14"/><circle cx="73" cy="46" r="3"/>
      </svg>
    </div>
    <div class="tech-label" style="left:228px;top:425px">IP Based Technology</div>

    <div class="tech-item" style="left:443px;top:372px">
      <svg width="90" height="58" viewBox="0 0 90 58" fill="none" stroke="#111" stroke-width="2.5">
        <path d="M10 26V8a6 6 0 0 1 6-6h58a6 6 0 0 1 6 6v18"/><path d="M14 26c2-8 24-8 26 0M50 26c2-8 24-8 26 0"/>
        <rect x="2" y="26" width="86" height="22"/><path d="M2 38h86M4 48v8M86 48v8"/>
      </svg>
    </div>
    <div class="tech-label" style="left:442px;top:460px">Home/Office/Hotel Automation</div>

    <div class="tech-item" style="left:651px;top:357px">
      <svg width="64" height="86" viewBox="0 0 64 86" fill="none" stroke="#111" stroke-width="2.5">
        <path d="M32 2l7 10 12-3-2 12 11 6-11 6 2 12-12-3-7 10-7-10-12 3 2-12L4 27l11-6-2-12 12 3z" fill="#111" stroke="none"/>
        <path d="M36 14l-10 16h9l-6 14 12-18h-9z" fill="#e2e2e2" stroke="none"/>
        <path d="M2 66q5-5 10 0t10 0 10 0 10 0 10 0 10 0M2 74q5-5 10 0t10 0 10 0 10 0 10 0 10 0M2 82q5-5 10 0t10 0 10 0 10 0 10 0 10 0"/>
      </svg>
    </div>
    <div class="tech-label" style="left:658px;top:457px">Electricity Power Meters</div>
  </section>

  <section class="sales" role="img" aria-label="Photo of a smiling businesswoman in a dark suit in a bright office, holding a pen and a printed bar chart">
    <div class="sales-title">SALES</div>
  </section>

  <footer class="site-footer">
    <nav class="footer-nav">
      <a href="#">Home</a><a href="#">About us</a><a href="#">Technology</a><a href="#">Services</a><a href="#">Products</a><a class="contact" href="#">Contact us</a>
    </nav>
    <p class="copyright">Copyright © 2014, All rights reserved</p>
    <div class="social"><span></span><span></span><span></span><span></span></div>
  </footer>
</body>
</html>
```